We need a web site design that is connected to Talbrook Roofing an American company, Veteran owned. Specializing in new roofs of all kinds, repair existing roofs and emergency roof repairs. located in the north Georgia mountains

Target Market(s)

homeowners end users, real estate, home owners insurance companies

Industry/Entity Type

roofing

Contact Information for Business Card

logo, Veteran owned, supports veteran charities, phone number ect

Font styles to use
Serif

Requirements
Should not have
• na

```html
<!DOCTYPE html>
<html lang="en">
<head>
<meta charset="utf-8">
<title>Talbrook Roofing – Business Card</title>
<link rel="stylesheet" href="https://fonts.googleapis.com/css2?family=Montserrat:wght@400;500;700;800&display=swap">
<style>
  :root {
    --bg: #2e2e2e;
    --gold-dark: #e0952a;
    --gold-light: #f3c554;
    --gold-line: #f0b733;
    --red: #d2321f;
    --ink: #1f1f1f;
    --white: #ffffff;
  }
  * { box-sizing: border-box; margin: 0; padding: 0; }
  html, body { width: 1200px; height: 875px; overflow: hidden; }
  body {
    background: var(--bg);
    font-family: "Montserrat", sans-serif;
    display: flex;
    flex-direction: column;
    align-items: center;
    justify-content: center;
    gap: 48px;
  }
  .card {
    width: 600px;
    height: 343px;
    border-radius: 22px;
    position: relative;
    overflow: hidden;
    box-shadow: 0 14px 30px rgba(0,0,0,.45);
  }
  /* Front */
  .card-front {
    background: linear-gradient(135deg, var(--gold-dark) 0%, #e9a93a 50%, var(--gold-light) 100%);
  }
  .front-mark {
    position: absolute;
    top: 104px;
    left: 0; right: 0;
    display: flex;
    align-items: center;
    justify-content: center;
    gap: 14px;
  }
  .mark-dot {
    width: 26px; height: 26px;
    border-radius: 50%;
    background: var(--red);
  }
  .brand-name {
    font-weight: 800;
    font-size: 40px;
    letter-spacing: 1px;
    color: var(--red);
    text-transform: uppercase;
    line-height: 1;
  }
  .tagline {
    position: absolute;
    bottom: 42px;
    left: 0; right: 0;
    text-align: center;
    color: var(--white);
    font-size: 13px;
    font-weight: 500;
    letter-spacing: .3px;
  }
  .tagline .divider {
    display: inline-block;
    width: 1.5px;
    height: 16px;
    background: var(--red);
    margin: 0 12px;
    vertical-align: middle;
  }
  /* Back */
  .card-back { background: var(--white); }
  .back-mark {
    position: absolute;
    top: 40px;
    right: 36px;
    display: flex;
    align-items: center;
    gap: 10px;
  }
  .back-mark .mark-dot { width: 18px; height: 18px; }
  .back-mark .brand-name { font-size: 24px; }
  .rule {
    position: absolute;
    left: 36px; right: 36px;
    top: 150px;
    height: 1.5px;
    background: var(--gold-line);
  }
  .person {
    position: absolute;
    left: 36px;
    top: 170px;
  }
  .person-name {
    font-size: 26px;
    font-weight: 700;
    color: var(--gold-line);
    line-height: 1.1;
  }
  .person-role {
    font-size: 14px;
    color: var(--ink);
    margin-top: 2px;
  }
  .contacts {
    list-style: none;
    position: absolute;
    left: 36px;
    bottom: 36px;
    font-size: 14px;
    color: var(--ink);
  }
  .contacts li {
    display: flex;
    align-items: center;
    gap: 9px;
    line-height: 1.6;
  }
  .contacts svg { width: 12px; height: 12px; fill: var(--red); flex: none; }
  .address {
    position: absolute;
    right: 36px;
    top: 172px;
    text-align: right;
    font-size: 14px;
    color: var(--ink);
    line-height: 1.45;
    font-style: normal;
  }
</style>
</head>
<body>
  <section class="card card-front" aria-label="Card front">
    <div class="front-mark">
      <span class="mark-dot"></span>
      <span class="brand-name">Talbrook Roofing</span>
    </div>
    <p class="tagline">Serving North Georgia Mountains<span class="divider"></span>Emergency Service Available 24/7</p>
  </section>

  <section class="card card-back" aria-label="Card back">
    <div class="back-mark">
      <span class="mark-dot"></span>
      <span class="brand-name">Talbrook Roofing</span>
    </div>
    <div class="rule"></div>
    <div class="person">
      <h1 class="person-name">Daniel Hart</h1>
      <p class="person-role">Owner</p>
    </div>
    <address class="address">12 Laurel Ridge Road, # 3 - 5<br>Ellijay, GA 30540</address>
    <ul class="contacts">
      <li>
        <svg viewBox="0 0 24 24" aria-hidden="true"><path d="M6.6 10.8a15 15 0 0 0 6.6 6.6l2.2-2.2a1 1 0 0 1 1-.25 11.4 11.4 0 0 0 3.6.57 1 1 0 0 1 1 1V20a1 1 0 0 1-1 1A17 17 0 0 1 3 4a1 1 0 0 1 1-1h3.5a1 1 0 0 1 1 1c0 1.25.2 2.45.57 3.6a1 1 0 0 1-.25 1z"/></svg>
        (08) 5550 1482
      </li>
      <li>
        <svg viewBox="0 0 24 24" aria-hidden="true"><path d="M2 5h20v14H2zm2 2v.5l8 5 8-5V7l-8 5z"/></svg>
        info@talbrookroofing.com
      </li>
      <li>
        <svg viewBox="0 0 24 24" aria-hidden="true"><circle cx="12" cy="12" r="10"/></svg>
        www.talbrookroofing.com
      </li>
    </ul>
  </section>
</body>
</html>
```